Web Design Project - ReelHarbor Style Website

Hi there, we want to create a ReelHarbor / Flickden style website. We have a logo, and will be using a similar structure to this platform; http://tapecrate.example/v2/
Please feel free to be creative as possible, and make the site look however you would like :) keeping in mind the Ad space, and user friendly layout. We would like
1) The main page and
2) the video view page
designed
Updates
Logo and stock image uploaded
Hello; we most likely be basing the site on this tape crate theme, which also works as a mobile version.
Another option that I found for a layout which is different :)
http://www.quillnest-studio.example/demo-theme.cfm?theme=marvane
One last update; really like this one too
I am 100% likely to now use this format;
Target Market(s)
Bars, Cafe's, Restaurants, Attractions, Venues, Pubs, Wine and Dine
Industry/Entity Type
Reelharbor
Requirements
Must have
- Can be similar to ReelHarbor, but closer to Flickden's funky fresh look.
Should not have
- Not be too cluttered with too many videos on the home page. Feel free to think outside the box

```html
<!DOCTYPE html>
<html lang="en">
<head>
<meta charset="utf-8">
<title>Bayside Reels — Video View</title>
<link rel="stylesheet" href="https://fonts.googleapis.com/css2?family=Cabin:wght@400;500;600;700&display=swap">
<style>
:root{
  --page-dark:#262626;
  --sky:#00bff0;
  --nav-blue:#0e6fbd;
  --panel-top:#e3f5fd;
  --panel-mid:#82d5f8;
  --panel-low:#dff3fc;
  --ink:#111;
  --muted:#555;
  --white:#fff;
  --field:#bfe6f8;
}
*{box-sizing:border-box;margin:0;padding:0}
html,body{width:960px;height:1200px;overflow:hidden}
body{background:var(--page-dark);font-family:"Cabin",sans-serif;color:var(--ink);position:relative}
.abs{position:absolute}
.site-header{left:0;top:0;width:960px;height:108px;background:var(--sky);border-bottom:2px solid #4aa9cc}
.brand{left:80px;top:30px;color:var(--white);font-size:40px;font-weight:600;letter-spacing:-1px;line-height:1}
.main-panel{left:83px;top:166px;width:797px;height:970px;
  background:linear-gradient(to bottom,var(--panel-top) 0%,var(--panel-mid) 40%,var(--panel-mid) 78%,var(--panel-low) 100%)}
.main-nav{left:74px;top:168px;width:816px;height:42px;background:var(--nav-blue);display:flex;align-items:center;padding-left:20px}
.main-nav a{color:var(--white);text-decoration:none;font-size:19px;margin-right:24px}
.search{left:659px;top:178px;width:176px;height:24px;background:#b9d9ee;border:1px solid #d6ebf7}
.search svg{position:absolute;right:6px;top:3px}
.player{left:139px;top:230px;width:445px;height:257px;border:3px solid var(--nav-blue);
  background:radial-gradient(circle at 25% 45%,#f4a0c8 0%,#6a2a48 22%,transparent 40%),
  radial-gradient(circle at 78% 40%,#2fbf5a 0%,#1b4a2a 20%,transparent 38%),
  radial-gradient(circle at 55% 55%,#c27a2a 0%,transparent 30%),#0b0b0b}
.play{left:190px;top:85px}
.video-info{left:594px;top:234px;width:216px;font-size:9.4px;line-height:11.6px}
.video-info h1{font-size:13px;font-weight:400;line-height:16px}
.video-info h2{font-size:11px;font-weight:500;line-height:13px}
.video-info h3{font-size:10px;font-weight:500;line-height:13px;margin-bottom:10px}
.video-info p{margin-bottom:23px}
.divider{left:139px;top:509px;width:680px;height:1px;background:#c7e8f7}
.section-title{font-size:13px;font-weight:400}
.related-title{left:139px;top:515px}
.thumb{top:536px;width:162px;height:94px;border:3px solid var(--nav-blue)}
.t1{left:141px;background:linear-gradient(100deg,#c0392b,#e67e22,#f1c40f,#8e44ad,#2980b9,#27ae60)}
.t2{left:317px;background:radial-gradient(circle at 40% 50%,#ff4fd8,#b01c6a 40%,#2a0a18)}
.t3{left:490px;background:linear-gradient(#c9d4db 0%,#8ba3b2 40%,#c6b9a4 100%)}
.t4{left:662px;background:radial-gradient(circle at 55% 40%,#f2c21b,#7a4a10 40%,#2e4a12)}
.category-band{left:74px;top:634px;width:816px;height:60px;background:var(--sky)}
.tab-corner{width:0;height:0;border-style:solid}
.cat{top:640px;width:84px;height:49px;background:linear-gradient(#fff,#e6e6e6);display:flex;align-items:center;justify-content:center;font-size:13px}
.arrow{top:653px}
.comments-title{left:138px;top:719px}
.avatar{left:138px;top:740px;width:44px;height:44px;background:linear-gradient(#5a3a2a,#c89a7e);border:1px solid #fff}
.comment-box{left:195px;top:740px;width:342px;height:45px;background:var(--white)}
.comment-box span{position:absolute;left:11px;top:6px;font-size:9px;color:#a8a8a8}
.comment{left:138px;width:404px;font-size:9.4px;line-height:11.6px}
.meta{left:138px;font-size:8px;color:var(--muted)}
.meta span{margin-left:14px}
.widget{left:568px;top:718px}
.widget-label{left:592px;width:200px;height:30px;background:var(--white);border:3px solid var(--nav-blue);font-size:13px;padding-left:18px;line-height:24px}
.widget-field{left:594px;width:196px;height:24px;background:var(--field);border-radius:3px;font-size:13px;color:#555;padding-left:18px;line-height:24px}
.ad-space{left:576px;top:926px;width:238px;height:160px;background:#d3eefb;border:3px solid #5aaee4;display:flex;align-items:center;justify-content:center;font-size:13px}
.footer-band{left:74px;top:1096px;width:816px;height:40px;background:var(--sky)}
.social{top:1102px;width:29px;height:29px;border-radius:5px}
</style>
</head>
<body>
<header class="site-header abs"><div class="brand abs">Bayside Reels</div></header>

<section class="main-panel abs"></section>

<nav class="main-nav abs">
  <a href="#">Home</a><a href="#">Layouts</a><a href="#">Blog</a><a href="#">Shortcuts</a><a href="#">Portfolio</a><a href="#">Contact</a>
</nav>
<div class="search abs">
  <svg width="20" height="18" viewBox="0 0 20 18"><circle cx="7" cy="7" r="5" fill="none" stroke="#fff" stroke-width="2.5"/><line x1="11" y1="11" x2="18" y2="16" stroke="#fff" stroke-width="3"/></svg>
</div>

<div class="player abs" role="img" aria-label="Featured video still: colourful blurred heart-shaped lights on dark background">
  <svg class="play abs" width="58" height="58" viewBox="0 0 58 58"><circle cx="29" cy="29" r="26" fill="#dbe9f5" stroke="#1a6fc0" stroke-width="4"/><path d="M21 15 L45 29 L21 43 Z" fill="#1a6fc0"/></svg>
</div>

<article class="video-info abs">
  <h1>Video Title</h1>
  <h2>Video Artist</h2>
  <h3>Video lenght</h3>
  <p>This is Pixelmarsh's version &nbsp;of Lorem Ipsum. Proin gravida nibh vel velit auctor aliquet. Aenean sollicitudin, lorem quis bibendum auctor, nisi elit consequat ipsum, nec sagittis sem nibh id elit. Duis sed odio sit amet nibh vulputate cursus a sit amet mauris. Morbi accumsan ipsum velit.</p>
  <p>Sed non &nbsp;mauris vitae erat consequat auctor eu in elit. Class aptent taciti sociosqu ad litora torquent per conubia nostra, per inceptos himenaeos. Mauris in erat justo. Nullam ac urna eu felis dapibus condimentum sit amet a augue. Sed non neque elit. Sed ut imperdiet nisi. Proin condimentum fermentum nunc. Etiam pharetra, erat sed fermentum feugiat, velit mauris egestas quam, ut aliquam massa nisl quis neque.</p>
</article>

<div class="divider abs"></div>
<h2 class="section-title related-title abs">Related Videos</h2>
<div class="thumb t1 abs" role="img" aria-label="Related video: colourful feathers"></div>
<div class="thumb t2 abs" role="img" aria-label="Related video: pink bokeh lights"></div>
<div class="thumb t3 abs" role="img" aria-label="Related video: horses running along a beach"></div>
<div class="thumb t4 abs" role="img" aria-label="Related video: golden pheasant"></div>

<div class="category-band abs"></div>
<div class="tab-corner abs" style="left:74px;top:624px;border-width:0 0 10px 9px;border-color:transparent transparent var(--sky) transparent"></div>
<div class="tab-corner abs" style="left:881px;top:624px;border-width:10px 0 0 9px;border-color:transparent transparent transparent var(--sky)"></div>
<svg class="arrow abs" style="left:160px" width="22" height="24" viewBox="0 0 22 24"><path d="M18 2 L4 12 L18 22 L12 12 Z" fill="var(--nav-blue)"/></svg>
<svg class="arrow abs" style="left:786px" width="22" height="24" viewBox="0 0 22 24"><path d="M4 2 L18 12 L4 22 L10 12 Z" fill="var(--nav-blue)"/></svg>
<div class="cat abs" style="left:212px">FUN</div>
<div class="cat abs" style="left:304px">HOT</div>
<div class="cat abs" style="left:394px">NEWS</div>
<div class="cat abs" style="left:486px">TRENDING</div>
<div class="cat abs" style="left:577px">MUSIC</div>
<div class="cat abs" style="left:666px">SOCIAL</div>

<h2 class="section-title comments-title abs">All Comments (37)</h2>
<div class="avatar abs" role="img" aria-label="Commenter profile photo"></div>
<div class="comment-box abs"><span>Add a Comment</span></div>

<p class="comment abs" style="top:799px">This is Pixelmarsh's version &nbsp;of Lorem Ipsum. Proin gravida nibh vel velit auctor aliquet. Aenean sollicitudin, lorem quis bibendum auctor, nisi elit consequat ipsum, nec sagittis sem nibh id elit. Duis sed odio sit amet nibh vulputate cursus a sit amet mauris. Morbi accumsan ipsum velit.</p>
<div class="meta abs" style="top:838px">user124asdf<span>1 hour ago</span></div>
<p class="comment abs" style="top:856px">Sed non &nbsp;mauris vitae erat consequat auctor eu in elit. Class aptent taciti sociosqu ad litora torquent per conubia nostra, per inceptos himenaeos. Mauris in erat justo. Nullam ac urna eu felis dapibus condimentum sit amet a augue. Sed non neque elit. Sed ut imperdiet nisi. Proin condimentum fermentum nunc. Etiam pharetra, erat sed fermentum feugiat, velit mauris egestas quam, ut aliquam massa nisl quis neque. Suspendisse in orci enim.</p>
<div class="meta abs" style="top:919px">user124asdf<span>1 hour ago</span></div>
<p class="comment abs" style="top:948px">This is Pixelmarsh's version &nbsp;of Lorem Ipsum. Proin gravida nibh vel velit auctor aliquet. Aenean sollicitudin, lorem quis bibendum auctor, nisi elit consequat ipsum, nec sagittis sem nibh id elit. Duis sed odio sit amet nibh vulputate cursus a sit amet mauris. Morbi accumsan ipsum velit.<br>auctor eu in elit.</p>
<div class="meta abs" style="top:999px">user124asdf<span>1 hour ago</span></div>

<svg class="widget abs" width="254" height="200" viewBox="0 0 254 200">
  <path d="M0 18 H64 V10 H110 V0 H146 V10 H190 V18 H254 V38 H246 V180 H254 V200 H0 V180 H8 V38 H0 Z" fill="#1fb0ec" stroke="var(--nav-blue)" stroke-width="2"/>
  <rect x="18" y="36" width="218" height="146" fill="#7fd4f8" stroke="var(--nav-blue)" stroke-width="2"/>
</svg>
<div class="widget-label abs" style="top:773px">Subscribe to our Newsletter</div>
<div class="widget-field abs" style="top:808px">Name@email.com</div>
<div class="widget-label abs" style="top:837px">Suggest yo you friend</div>
<div class="widget-field abs" style="top:870px">Name@email.com</div>

<div class="ad-space abs">SPACE for Advertise</div>

<div class="footer-band abs"></div>
<div class="tab-corner abs" style="left:74px;top:1086px;border-width:0 0 10px 9px;border-color:transparent transparent var(--sky) transparent"></div>
<div class="tab-corner abs" style="left:881px;top:1086px;border-width:10px 0 0 9px;border-color:transparent transparent transparent var(--sky)"></div>
<a class="social abs" href="#" aria-label="Social link" style="left:680px;background:#3b5b9a"></a>
<a class="social abs" href="#" aria-label="Feed link" style="left:716px;background:#f08a24"></a>
<a class="social abs" href="#" aria-label="Social link" style="left:751px;background:#5fc4ea"></a>
<a class="social abs" href="#" aria-label="Social link" style="left:786px;background:#1e6aa8"></a>
</body>
</html>
```